Design for Torvel Ginger Chewy Candy!

Hello! We are Torvel Enterprises Corp, a food manufacturer and distributor based in Los Angeles, CA. We manufacture Chips, Cookies, Juices, Dairy, and last but not least, Candies! We are launching our Ginger Chewy Candy soon and we need a great design for it!

Our Ginger Chewy Candy is a perfect mixture between sweet and spicy from the ginger itself. Torvel Ginger Chewy Candy a good relief for sore throat and nausea.

Now, other than a great design, we also welcome brand suggestions for the candy.
If you can come up with a logo for the Ginger Candy, that would be swell!

We are open to unique and out of the box design. We chose a few color schemes for the design, but feel free to step out of the box if you feel it suits the brand.

We don't have the exact size for the plastic pouch, but it should be a generic small plastic pouch size (approximately 4 oz resealable plastic pouch)

Please have fun designing the project, we can't wait to see all the great designs!

Cheers!

Target Market(s)

USA and Asian market
Age 30-70
Male and Female

Industry/Entity Type

Manufacture

Font styles to use
Serif
Sans Serif
Decorative

Colors
fff3d1
fee18a
fece3e
fbc994
fce8d3

Requirements
Must have
• Torvel Logo
• A picture of ginger (illustrations or photographs are welcome)
Nice to have
• Coating suggestions like Matte surface or SPOT UV
• Give us ideas of what the name of the chewy candy should be. Product name ideas are welcome!

```html
<!DOCTYPE html>
<html lang="en">
<head>
<meta charset="utf-8">
<title>Torvel Ginger Chewy Candy – Pouch Front</title>
<link rel="stylesheet" href="https://fonts.googleapis.com/css2?family=Cinzel:wght@700&family=Amatic+SC:wght@700&display=swap">
<style>
  :root {
    --stage: #ececea;
    --band-orange: #e8651f;
    --band-light: #f28a45;
    --swirl-center: #fff0b0;
    --swirl-mid: #fece3e;
    --swirl-edge: #f6a93a;
    --ginger-green: #1f6b2a;
    --brand-blue: #1f4fa8;
    --leaf-green: #5aa83a;
    --label-dark: #3a3a3a;
    --label-text: #fee18a;
    --art-tone-a: #f3d9a6;
    --art-tone-b: #e8b86a;
  }
  * { margin: 0; padding: 0; box-sizing: border-box; }
  html, body { width: 1200px; height: 1200px; overflow: hidden; background: var(--stage); }
  .canvas { position: relative; width: 1200px; height: 1200px; }
  .pouch-front {
    position: absolute; left: 272px; top: 30px; width: 656px; height: 1140px;
    overflow: hidden; border-radius: 14px 14px 6px 6px;
    background: radial-gradient(ellipse 70% 55% at 50% 51%, var(--swirl-center) 0%, var(--swirl-mid) 45%, var(--swirl-edge) 100%);
  }
  .swirl-pattern { position: absolute; inset: 0; }
  .top-band { position: absolute; left: 0; top: 0; width: 656px; height: 200px; }
  .brand-lockup {
    position: absolute; left: 0; right: 0; top: 235px;
    display: flex; justify-content: center; align-items: center; gap: 18px;
  }
  .brand-dot { width: 26px; height: 26px; border-radius: 50%; background: var(--leaf-green); }
  .brand-name {
    font-family: "Cinzel", serif; font-weight: 700; font-size: 92px;
    color: var(--brand-blue); line-height: 1;
  }
  .product-title {
    position: absolute; left: 0; right: 0; top: 418px; text-align: center;
    font-family: "Cinzel", serif; font-weight: 700; color: var(--ginger-green);
  }
  .product-name { font-size: 96px; letter-spacing: 4px; line-height: 1; }
  .product-type { font-size: 31px; letter-spacing: 2px; margin-top: 8px; line-height: 1; }
  .ginger-art {
    position: absolute; left: 100px; top: 645px; width: 390px; height: 310px;
    border-radius: 40% 45% 38% 42%;
    background: radial-gradient(ellipse at 50% 55%, var(--art-tone-a) 0%, var(--art-tone-b) 70%, rgba(232,184,106,0) 100%);
  }
  .tasty-label { position: absolute; left: 195px; top: 985px; width: 255px; height: 70px; }
  .tasty-text {
    position: absolute; left: 0; right: 0; top: 0; height: 70px;
    display: flex; align-items: center; justify-content: center;
    font-family: "Amatic SC", sans-serif; font-weight: 700; font-size: 50px;
    color: var(--label-text); letter-spacing: 2px;
  }
</style>
</head>
<body>
<div class="canvas">
  <div class="pouch-front">
    <svg class="swirl-pattern" viewBox="0 0 656 1140" role="img" aria-label="Decorative swirling sunburst stripes in yellow and orange">
      <rect width="656" height="1140" fill="none"/>
    </svg>

    <svg class="top-band" viewBox="0 0 656 200" aria-hidden="true">
      <defs>
        <linearGradient id="bandFill" x1="0" y1="0" x2="1" y2="0">
          <stop offset="0" stop-color="var(--band-orange)"/>
          <stop offset="1" stop-color="var(--band-light)"/>
        </linearGradient>
      </defs>
      <path fill="url(#bandFill)" d="M0 0 H656 V190 L640 150 L625 175 L610 110 L590 140 L575 60 L560 100 L540 70 L520 120 L500 75 L480 130 L460 90 L440 140 L420 95 L400 150 L380 100 L360 145 L340 110 L320 150 L300 105 L280 140 L262 70 L240 125 L222 80 L200 140 L180 95 L160 135 L140 90 L120 140 L100 100 L80 150 L60 110 L40 150 L20 100 L0 150 Z"/>
    </svg>

    <div class="brand-lockup">
      <span class="brand-dot"></span>
      <span class="brand-name">Torvel</span>
    </div>

    <div class="product-title">
      <div class="product-name">GINGER</div>
      <div class="product-type">CHEWY CANDY</div>
    </div>

    <div class="ginger-art" role="img" aria-label="Illustration of ginger root with sliced pieces and green leaves"></div>

    <div class="tasty-label">
      <svg viewBox="0 0 255 70" width="255" height="70" aria-hidden="true">
        <path fill="var(--label-dark)" d="M20 12 L245 4 L232 22 L250 30 L236 46 L248 58 L30 66 L5 60 L24 50 L0 38 L22 28 L8 18 Z"/>
      </svg>
      <div class="tasty-text">TASTY</div>
    </div>
  </div>
</div>
</body>
</html>
```